Website design for headhunting agency

The design I need (PSD file) is for a company offering specialised services in recruitment of high-end executive and management positions for businesses.
OBJECTIVES OF THE WEBSITE:
1. Let entrepreneurs and business leaders know about their services and easily have them contact Varolinq if they want more information about their services.
2. Display a list of available carreer opportunities (according to their client's need).
WHAT I NEED:
1st, I need the design for the Home Page ONLY. Once approved, I will need the other pages designed as well. (Here is prototype that we've already developed for the Website that will guide you in the design:
http://demo.pelvarshop.net/varolinq/fr/accueil)
ATTACHED FILES
- Logo
- PDF brochure: Use for inspiration. It is encouraged that you use pictures from this brochure. You can always suggest new ones, as long as they are not expensive to buy and have the same look and feel as the brochure.
HOMEPAGE:
1. Main menu : 6 sections
Accueil | Varolinq | Équipe | Approche | Postes disponibles | Publications
2. Main slider: 4 sections
- Chasseurs de têtes (Headhunters)
- Notre approche (Our Approach)
- Postes cadres disponibles (Executive Careers
Opportunities)
- Contactez-nous (Contact Us)
3. Main Call To Action Boxes :
- Liste Des postes disponibles (Liste of Available Careers
Opportunities)
- Formulaire de contact (contact form)
4. Latest blog articles
- Les derniers articles.
OTHER PAGES (to design once Homepage is approved)
- Varolinq (about us)
- Équipe (our team)
- Approche (our approach)
- Postes disponibles (Career opportunities)
- Publications (blog articles)
- Contact (Contact us)
Target Market(s)
ORGANIZATIONS:
Leaders of organizations seeking to recruit highly qualified staff.
HIGHLY QUALIFIED RESOURCES:
Senior individuals seeking a salary between $70,000 and $ $200,000 annually
PROFESSIONAL SECTORS:
manufacturing : Primary and secondary industries
pharmaceutical
Aerospace
Finances
Retail business
Engineering
Chemical and petrochemical
IT, telecommunications and high technology
Professional Organizations and Association
Industry/Entity Type
Business
Look and feel
Each slider illustrates characteristics of the customer's brand and the style your logo design should communicate.

```html
<!DOCTYPE html>
<html lang="fr">
<head>
<meta charset="utf-8">
<title>Varolinq – Recherche de cadres</title>
<link href="https://fonts.googleapis.com/css2?family=Signika:wght@300;400;600&display=swap" rel="stylesheet">
<style>
:root{
  --bar-dark:#2a2a2a;
  --bar-mid:#3a3a3a;
  --teal:#1b6a7a;
  --teal-dark:#155c6a;
  --gold:#c9960c;
  --text:#4a4a4a;
  --muted:#7a7a7a;
  --line:#e2e2e2;
  --band:#eeeeee;
  --white:#ffffff;
  --blue-top:#3a94c6;
  --blue-bot:#1f6ea3;
  --grey-top:#7d838b;
  --grey-bot:#50565e;
}
*{box-sizing:border-box;margin:0;padding:0}
html,body{width:841px;height:1200px;overflow:hidden}
body{position:relative;background:var(--white);font-family:'Signika',Arial,sans-serif;color:var(--text);font-size:10px}
.abs{position:absolute}

.topbar{left:0;top:0;width:841px;height:40px;background:linear-gradient(#3b3b3b,#262626)}
.topnav{right:62px;top:0;height:40px;display:flex;border-left:1px solid #1a1a1a}
.topnav span{display:flex;align-items:center;padding:0 12px;color:#e8e8e8;font-size:10.5px;border-right:1px solid #1a1a1a;box-shadow:inset 1px 0 0 #474747}
.flag{width:16px;height:11px;background:#2d3f86;margin-right:6px;position:relative}
.flag::after{content:"";position:absolute;left:0;top:4px;width:16px;height:3px;background:#c8283a}
.caret{width:0;height:0;border-left:4px solid transparent;border-right:4px solid transparent;border-top:5px solid #ddd;margin-left:8px}

.header{left:0;top:40px;width:841px;height:107px;background:linear-gradient(#ffffff 50%,#f1f1f1 50%)}
.brand{left:63px;top:52px}
.brand .name{display:flex;align-items:center;gap:8px;color:var(--teal);font-size:27px;font-weight:400;letter-spacing:.5px}
.brand .mark{width:12px;height:12px;background:var(--gold)}
.brand .tag{margin-left:68px;color:#777;font-size:11px;font-weight:300}
.mainnav{right:62px;top:112px;display:flex}
.mainnav span{padding:0 14px;font-size:12px;color:var(--teal-dark);border-left:1px solid #d6d6d6;line-height:20px}
.mainnav span:first-child{border-left:none;color:var(--gold)}
.mainnav span:last-child{padding-right:0}

.hero{left:0;top:147px;width:841px;height:237px;background:radial-gradient(ellipse at 62% 40%,#d6d8da,#a9acaf 85%)}
.hero h1{left:64px;top:46px;width:440px;color:#fff;font-size:21.5px;font-weight:600;line-height:26px;text-shadow:0 1px 2px rgba(0,0,0,.35)}
.btn-more{left:65px;top:113px;width:102px;height:30px;border-radius:3px;background:linear-gradient(#4a4a4a,#2e2e2e);color:#eee;font-size:12px;display:flex;align-items:center;padding-left:10px;gap:8px}
.btn-more i{width:14px;height:14px;border-radius:50%;background:#1c1c1c;display:flex;align-items:center;justify-content:center}
.portrait{left:520px;top:0;width:245px;height:237px;background:linear-gradient(#b99f8d 0%,#8e7e76 55%,#a69a92 100%);border-radius:120px 120px 0 0}
.dots{left:64px;top:202px;display:flex;gap:5px}
.dots i{width:11px;height:11px;border-radius:50%;border:1px solid #888;background:#d2d2d2}
.dots i:first-child{background:#444}

.h2{color:var(--teal-dark);font-size:17px;font-weight:600}
.panel{background:#fff;border:1px solid var(--line);box-shadow:0 0 4px rgba(0,0,0,.06)}
.jobs{left:62px;top:436px;width:345px;height:254px;padding:14px 20px 0 18px}
.job{display:flex;gap:7px;margin-bottom:9px}
.job .arr{color:#555;font-size:8px;padding-top:3px}
.job p{font-size:9.5px;line-height:14px;color:#444}
.job .date{color:var(--muted);margin-top:4px}

.contact{left:432px;top:436px;width:345px;height:254px}
.field-label{left:26px;font-size:10.5px;color:#666}
.input{left:90px;width:234px;height:30px;border:1px solid #d8d8d8;border-radius:2px;background:linear-gradient(#fff 80%,#efefef)}
.submit{left:259px;top:205px;width:66px;height:29px;border-radius:3px;background:linear-gradient(#9a9a9a,#6c6c6c);color:#fff;font-size:11.5px;font-weight:600;display:flex;align-items:center;justify-content:center}

.band{left:0;top:715px;width:841px;height:331px;background:var(--band);border-top:1px solid #e2e2e2;border-bottom:1px solid #e2e2e2}
.band-title{left:0;top:29px;width:841px;text-align:center}
.article{width:345px;height:114px;display:flex;gap:13px;padding:12px 14px 0 17px}
.thumb{width:90px;height:90px;border:2px solid #fff;box-shadow:0 0 3px rgba(0,0,0,.25);flex:none}
.article h3{color:var(--gold);font-size:11.5px;font-weight:400;margin:5px 0 7px}
.article p{font-size:9.5px;line-height:14.5px;color:#444}
.article .date{color:var(--muted);margin-top:3px}

.cta{top:1068px;width:344px;height:48px;border-radius:3px;display:flex;align-items:center;justify-content:center;gap:10px;color:#fff;font-size:16.5px;font-weight:600}
.cta.follow{left:63px;background:linear-gradient(var(--blue-top),var(--blue-bot))}
.cta.news{left:434px;background:linear-gradient(var(--grey-top),var(--grey-bot))}
.sq{width:18px;height:18px;background:#fff;border-radius:2px}

.footer{left:0;top:1130px;width:841px;height:70px;background:linear-gradient(#3a3a3a,#262626)}
.footer .copy{left:63px;top:33px;color:#ddd;font-size:10px}
.footer .fbrand{right:62px;top:24px;text-align:right;color:#9a9a9a}
.footer .fbrand b{display:block;font-weight:300;font-size:17px;letter-spacing:.5px}
.footer .fbrand small{font-size:7px}
</style>
</head>
<body>

<div class="abs topbar">
  <nav class="abs topnav">
    <span>Accueil</span><span>Plan du site</span><span>Code d'étique</span><span>Contact</span>
    <span><i class="flag"></i>English<i class="caret"></i></span>
  </nav>
</div>

<header class="abs header"></header>
<div class="abs brand">
  <div class="name"><i class="mark"></i>VAROLINQ</div>
  <div class="tag">Recherche de cadres</div>
</div>
<nav class="abs mainnav">
  <span>Accueil</span><span>Varolinq</span><span>Équipe</span><span>Approche</span><span>Postes disponibles</span><span>Publications</span>
</nav>

<section class="abs hero">
  <div class="abs portrait" role="img" aria-label="Photo of a smiling businesswoman wearing glasses and a grey blazer"></div>
  <h1 class="abs">Integer vulputate, mauris in luctus semper, diam nisl volutpat sem.</h1>
  <div class="abs btn-more">Know more <i><svg width="6" height="8" viewBox="0 0 6 8"><path d="M1 1l3 3-3 3" stroke="#fff" stroke-width="1.5" fill="none"/></svg></i></div>
  <div class="abs dots"><i></i><i></i><i></i><i></i></div>
</section>

<h2 class="abs h2" style="left:68px;top:404px">Liste des postes disponibles</h2>
<div class="abs panel jobs">
  <div class="job"><span class="arr">▶▶</span><div><p>Nunc tincidunt non elit ac vestibulum. Maecenas eget vehicula urna. Nulla facilisi. Nullam convallis, velit nec viverra.</p><p class="date">August-3-2013</p></div></div>
  <div class="job"><span class="arr">▶▶</span><div><p>Nunc tincidunt non elit ac vestibulum. Maecenas eget vehicula urna. Nulla facilisi. Nullam convallis, velit nec viverra.</p><p class="date">August-3-2013</p></div></div>
  <div class="job"><span class="arr">▶▶</span><div><p>Nunc tincidunt non elit ac vestibulum. Maecenas eget vehicula urna. Nulla facilisi. Nullam convallis, velit nec viverra.</p><p class="date">August-3-2013</p></div></div>
  <div class="job"><span class="arr">▶▶</span><div><p>Nunc tincidunt non elit ac vestibulum. Maecenas eget vehicula urna. Nulla facilisi. Nullam convallis, velit nec viverra.</p><p class="date">August-3-2013</p></div></div>
</div>

<h2 class="abs h2" style="left:438px;top:404px">Formulaire de contact</h2>
<form class="abs panel contact">
  <label class="abs field-label" style="top:24px">Name :</label><div class="abs input" style="top:18px"></div>
  <label class="abs field-label" style="top:63px">E-mail :</label><div class="abs input" style="top:57px"></div>
  <label class="abs field-label" style="top:102px">Phone :</label><div class="abs input" style="top:96px"></div>
  <label class="abs field-label" style="top:142px">Message :</label><div class="abs input" style="top:135px;height:58px"></div>
  <div class="abs submit">SUBMIT</div>
</form>

<section class="abs band">
  <h2 class="abs h2 band-title">Les derniers articles</h2>
  <article class="abs panel article" style="left:62px;top:54px">
    <div class="thumb" role="img" aria-label="Photo of a team of business people" style="background:linear-gradient(#dfe6ee,#8d98a6)"></div>
    <div><h3>Phasellus non tellus sollicitudin, ultricies</h3><p>Nunc tincidunt non elit ac vestibulum. Maecenas eget vehicula urna. Nulla facilisi. Nullam convallis, velit nec viverra.</p><p class="date">August-3-2013</p></div>
  </article>
  <article class="abs panel article" style="left:432px;top:54px">
    <div class="thumb" role="img" aria-label="Photo of a businessman working at a desk" style="background:linear-gradient(#f2f2f2,#b8b2ac)"></div>
    <div><h3>Phasellus non tellus sollicitudin, ultricies</h3><p>Nunc tincidunt non elit ac vestibulum. Maecenas eget vehicula urna. Nulla facilisi. Nullam convallis, velit nec viverra.</p><p class="date">August-3-2013</p></div>
  </article>
  <article class="abs panel article" style="left:62px;top:193px">
    <div class="thumb" role="img" aria-label="Illustration of business figures standing on puzzle pieces" style="background:linear-gradient(#f5f7fa,#b6c2d0)"></div>
    <div><h3>Phasellus non tellus sollicitudin, ultricies</h3><p>Nunc tincidunt non elit ac vestibulum. Maecenas eget vehicula urna. Nulla facilisi. Nullam convallis, velit nec viverra.</p><p class="date">August-3-2013</p></div>
  </article>
  <article class="abs panel article" style="left:432px;top:193px">
    <div class="thumb" role="img" aria-label="Photo of a cheerful man at a laptop" style="background:linear-gradient(#f0eeee,#c25050)"></div>
    <div><h3>Phasellus non tellus sollicitudin, ultricies</h3><p>Nunc tincidunt non elit ac vestibulum. Maecenas eget vehicula urna. Nulla facilisi. Nullam convallis, velit nec viverra.</p><p class="date">August-3-2013</p></div>
  </article>
</section>

<div class="abs cta follow"><i class="sq"></i>Suivez-nous sur Netlinko</div>
<div class="abs cta news">
  <svg width="24" height="17" viewBox="0 0 24 17"><rect x="0.5" y="0.5" width="23" height="16" fill="#fff"/><path d="M1 1l11 9 11-9" stroke="#9aa0a7" fill="none"/></svg>
  Inscrivez-vous à l'infolettre
</div>

<footer class="abs footer">
  <div class="abs copy">© Varolinq - Tous droits réservés</div>
  <div class="abs fbrand"><b>VAROLINQ</b><small>Recherche de cadres</small></div>
</footer>

</body>
</html>
```